Fun relaxed Travel Photography Business Card*

Require a fun, funky and quirky but rememberable business card for a travel photographer

Industry/Entity Type

Photographer

Contact Information for Business Card

Front Card

(my name) Tavo M.

Travel Photographer ( small under travel photographer) “self-proclaimed”

(website logo) wanderingtavo.example

(Instagram logo) @wandering_with_tavo

(Instagram logo) @wandering_with_tavo_2.0 (backup for when Instagram puts Tavo on timeout for bad behaviour)

Tel: N/A (removing the potential awkwardness of me not replying)

Email: (see above)

Back Card

Offending people since 1986

(Bottom right corner) “p.s. travelling made me fatTER”

Font styles to use
Serif

Colors

Designer to choose colors to be used in the design.

Requirements
Must have
• a camera
• a similar cartoon version of me as the "logo" see attached files, try to make as similar as possible

```html
<!DOCTYPE html>
<html lang="en">
<head>
<meta charset="utf-8">
<title>Tavo M. — Travel Photographer Business Card</title>
<link rel="stylesheet" href="https://fonts.googleapis.com/css2?family=Montserrat:wght@400;500;600;700&display=swap">
<style>
  :root {
    --stage: #1e1e1e;
    --card: #353535;
    --gold: #f2b829;
    --white: #f4f4f4;
    --art-light: #f5bf3a;
    --art-dark: #5a3a24;
  }
  * { box-sizing: border-box; margin: 0; padding: 0; }
  html, body { width: 1200px; height: 881px; overflow: hidden; }
  body {
    background: var(--stage);
    font-family: "Montserrat", sans-serif;
    display: flex;
    align-items: center;
    justify-content: center;
    gap: 40px;
  }
  .card {
    position: relative;
    width: 530px;
    height: 303px;
    background: var(--card);
    border-radius: 22px;
    box-shadow: 0 6px 0 var(--gold), 0 18px 30px rgba(0,0,0,.55);
    overflow: hidden;
  }

  /* Illustration side */
  .mascot-art {
    position: absolute;
    left: 195px;
    top: 38px;
    width: 150px;
    height: 160px;
    border-radius: 18px;
    background: radial-gradient(circle at 45% 35%, var(--art-dark) 0 26%, var(--art-light) 27% 100%);
  }
  .taglines {
    position: absolute;
    left: 0; right: 0;
    bottom: 26px;
    display: flex;
    justify-content: center;
    align-items: center;
    gap: 12px;
    font-size: 13px;
    font-weight: 600;
    letter-spacing: .04em;
    text-transform: uppercase;
  }
  .tagline-main { color: var(--gold); }
  .tagline-ps { color: var(--white); }
  .tagline-divider { width: 1px; height: 16px; background: var(--white); }

  /* Contact side */
  .identity {
    position: absolute;
    left: 44px;
    top: 112px;
    width: 190px;
    text-align: center;
  }
  .name {
    color: var(--gold);
    font-size: 30px;
    font-weight: 700;
    letter-spacing: .12em;
    line-height: 1;
  }
  .role {
    color: var(--white);
    font-size: 14px;
    margin-top: 6px;
    letter-spacing: .02em;
  }
  .identity-divider {
    position: absolute;
    left: 258px;
    top: 96px;
    width: 2px;
    height: 92px;
    background: var(--gold);
  }
  .contact-list {
    position: absolute;
    left: 278px;
    top: 92px;
    list-style: none;
    color: var(--white);
    font-size: 13px;
    line-height: 24px;
  }
  .contact-list li { display: flex; align-items: center; gap: 9px; }
  .contact-icon { width: 12px; height: 12px; flex: none; }
  .contact-icon path, .contact-icon circle, .contact-icon rect { stroke: var(--gold); fill: none; stroke-width: 1.4; }
</style>
</head>
<body>

  <section class="card card-illustration">
    <div class="mascot-art" role="img" aria-label="Cartoon mascot of the photographer relaxing on a yellow lounge chair beside a small table with a drink"></div>
    <div class="taglines">
      <span class="tagline-main">Offending people since 1986</span>
      <span class="tagline-divider"></span>
      <span class="tagline-ps">P.S. Travelling made me fatter</span>
    </div>
  </section>

  <section class="card card-contact">
    <div class="identity">
      <h1 class="name">TAVO M</h1>
      <p class="role">Travel Photographer</p>
    </div>
    <div class="identity-divider"></div>
    <ul class="contact-list">
      <li>
        <svg class="contact-icon" viewBox="0 0 12 12"><path d="M2 1.5 L4 1.5 L5 4 L3.8 5 Q5 7.5 7 8.2 L8 7 L10.5 8 L10.5 10 Q5 10.5 2 4 Z"/></svg>
        <span>+000 5550 - 0142</span>
      </li>
      <li>
        <svg class="contact-icon" viewBox="0 0 12 12"><rect x="1.5" y="1.5" width="9" height="9"/></svg>
        <span>@wandering_with_tavo</span>
      </li>
      <li>
        <svg class="contact-icon" viewBox="0 0 12 12"><rect x="1" y="2.5" width="10" height="7"/><path d="M1 2.5 L6 6.5 L11 2.5"/></svg>
        <span>info@wanderingtavo.example</span>
      </li>
      <li>
        <svg class="contact-icon" viewBox="0 0 12 12"><circle cx="6" cy="6" r="4.8"/><path d="M1.2 6 H10.8 M6 1.2 Q3 6 6 10.8 M6 1.2 Q9 6 6 10.8"/></svg>
        <span>www.wanderingtavo.example</span>
      </li>
    </ul>
  </section>

</body>
</html>
```